Homes, Invest in Non-performing loans

We need only 3 web pages, one for the home, one for the content, one for the properties.
The main focus of our business is to offer non performing loans (before foreclosures) to the general public. All the non-performing mortgages will end in a house, an apartment, a store, etc.
Our customers are able to invest from 10,000usd to 1,000,000usd (average 50,000usd).
Our customers' usual focus groups are employees who want second earnings, perceiving the business feeling without outlay time. They look for a solid finance sense corporation that confers them certainty.
Nearly all our clients desire the house, apartment, store, etc. more than the actual earnings.
The name of our company is BRAMLEY
Reason: We value the time and effort you already invest in our project. We realize that we did't come back on some of the doubts requested by the designers. It will be inequitable to the designers who prerequisite our feedback. We also appreciate the comprehension of the community in this postponement.
Reason: Designers,
We really apreciate all the time and effort you put on our project. From the begining we ask for 3 pages, so now we will leave the 10 finalist and provide some extra time to submit the other 2 pages.
We will race the price in 10%
Target Market(s)
Our customers average investors works as employees and want to have a second income or business without spending time. (People from 35 to 50)
Industry/Entity Type
Finance
Requirements
Should not have
- FLASH

```html
<!DOCTYPE html>
<html lang="en">
<head>
<meta charset="utf-8">
<title>Bramley — Homes Investment and Loans</title>
<link href="https://fonts.googleapis.com/css2?family=Cormorant+Garamond:wght@600;700&family=Sorts+Mill+Goudy&display=swap" rel="stylesheet">
<style>
  :root {
    --backdrop: #474747;
    --bar-dark: #1f1f1f;
    --panel-dark: #222222;
    --olive: #7a7728;
    --olive-line: #b8b88f;
    --paper: #ffffff;
    --ink: #111111;
    --light-text: #f2f2f2;
    --rule-dark: #0c0c0c;
  }
  * { margin: 0; padding: 0; box-sizing: border-box; }
  html, body { width: 1200px; height: 1000px; overflow: hidden; }
  body {
    background: var(--backdrop);
    font-family: "Sorts Mill Goudy", Georgia, serif;
    position: relative;
  }
  .page { position: absolute; left: 130px; top: 0; width: 940px; height: 1000px; }

  .top-bar {
    position: absolute; left: 0; top: 0; width: 940px; height: 34px;
    background: var(--bar-dark); border-top: 5px solid var(--olive);
  }
  .nav a {
    position: absolute; color: var(--light-text); text-decoration: none;
    font-size: 13px; letter-spacing: 1px; transform: translateX(-50%);
    text-shadow: 0 1px 2px #000;
  }
  .top-bar .nav a { top: 8px; }

  .header {
    position: absolute; left: 0; top: 34px; width: 940px; height: 564px;
    background: var(--paper);
  }
  .brand {
    position: absolute; left: 80px; top: 88px;
    display: flex; align-items: center; gap: 10px;
    font-size: 36px; color: var(--ink); letter-spacing: 2px;
  }
  .brand-mark { width: 18px; height: 18px; background: var(--olive); }
  .headline {
    position: absolute; left: 355px; top: 50px;
    font-family: "Cormorant Garamond", Georgia, serif; font-weight: 700;
    font-variant: small-caps; font-size: 40px; color: var(--ink); letter-spacing: 1px;
  }
  .intro {
    position: absolute; left: 357px; top: 103px; width: 460px;
    font-size: 16px; line-height: 20.5px; color: var(--ink); letter-spacing: 0.4px;
  }
  .header-rule {
    position: absolute; left: 41px; top: 227px; width: 858px; height: 2px;
    background: var(--olive-line);
  }
  .photo { position: absolute; box-shadow: 0 3px 6px rgba(0,0,0,0.45); }
  .photo-left { left: 11px; top: 290px; width: 245px; height: 225px;
    background: linear-gradient(180deg, #c9a79a 0%, #6b6f76 35%, #8b7d6c 65%, #5d7a45 88%, #8a8590 100%); }
  .photo-right { left: 682px; top: 290px; width: 247px; height: 233px;
    background: linear-gradient(180deg, #b7c7e0 0%, #c9a274 30%, #b58a5c 70%, #d8d6cf 100%); }
  .photo-main { left: 256px; top: 244px; width: 426px; height: 300px; z-index: 2;
    background: linear-gradient(180deg, #6fa2d6 0%, #a9c6df 22%, #8f7b66 45%, #4f7a33 70%, #e6e2d8 100%); }

  .content {
    position: absolute; left: 0; top: 598px; width: 940px; height: 376px;
    background: var(--panel-dark);
  }
  .rule-dark { position: absolute; left: 41px; width: 858px; height: 2px; background: var(--rule-dark); }
  .rule-top { top: 24px; }
  .rule-bottom { top: 339px; }
  .divider { position: absolute; left: 620px; top: 48px; width: 2px; height: 258px; background: var(--rule-dark); }
  .content h2 {
    position: absolute; font-weight: normal; color: var(--light-text); letter-spacing: 1px;
  }
  .main-title { left: 68px; top: 60px; font-size: 24px; }
  .body-copy {
    position: absolute; width: 400px; font-size: 14px; line-height: 20.5px;
    color: var(--light-text); letter-spacing: 0.5px;
  }
  .copy-one { left: 68px; top: 109px; }
  .copy-two { left: 66px; top: 204px; }
  .featured-title { left: 671px; top: 52px; font-size: 19px; }
  .featured-photo {
    position: absolute; left: 671px; top: 94px; width: 220px; height: 147px;
    background: linear-gradient(180deg, #1d4fa0 0%, #5a86c4 40%, #d9cdbd 62%, #5f8a3b 85%, #b8b3a6 100%);
  }
  .featured-caption { left: 671px; top: 251px; width: 230px; }
  .content .nav a { top: 352px; }

  .footer-band {
    position: absolute; left: 0; top: 974px; width: 940px; height: 26px; background: var(--olive);
  }
</style>
</head>
<body>
<div class="page">
  <header class="top-bar">
    <nav class="nav">
      <a href="#" style="left:383px">HOME</a>
      <a href="#" style="left:501px">PLANS</a>
      <a href="#" style="left:640px">PROPERTIES</a>
    </nav>
  </header>

  <section class="header">
    <div class="brand"><span class="brand-mark"></span>BRAMLEY</div>
    <h1 class="headline">Homes Investment and Loans</h1>
    <p class="intro">Lorem ipsum dolor sit amet, consectetur adipiscing elit. Integer eleifend magna eu est condimentum egestas. Donec euismod porttitor tristique. Nullam metus orci, rutrum sit amet hendrerit id,</p>
    <div class="header-rule"></div>
    <div class="photo photo-left" role="img" aria-label="Stone house with grey roof at dusk"></div>
    <div class="photo photo-main" role="img" aria-label="Large stone-front house with garden and driveway under blue sky"></div>
    <div class="photo photo-right" role="img" aria-label="Two-storey stucco house with tiled roof and garage"></div>
  </section>

  <section class="content">
    <div class="rule-dark rule-top"></div>
    <h2 class="main-title">Lorem ipsum dolor.</h2>
    <p class="body-copy copy-one">Lorem ipsum dolor sit amet, consectetur adipiscing elit. Integer eleifend magna eu est condimentum egestas. Donec euismod porttitor tristique. Nullam metus orci, rutrum sit amet hendrerit id,</p>
    <p class="body-copy copy-two">Lorem ipsum dolor sit amet, consectetur adipiscing elit. Integer eleifend magna eu est condimentum egestas. Donec euismod porttitor tristique. Nullam metus orci, rutrum sit amet hendrerit id,</p>
    <div class="divider"></div>
    <h2 class="featured-title">Featured Homes</h2>
    <div class="featured-photo" role="img" aria-label="Featured suburban home with double garage"></div>
    <p class="body-copy featured-caption">Lorem ipsum dolor sit amet, consectetur adipiscing elit.</p>
    <div class="rule-dark rule-bottom"></div>
    <nav class="nav">
      <a href="#" style="left:316px">HOME</a>
      <a href="#" style="left:471px">PLANS</a>
      <a href="#" style="left:647px">PROPERTIES</a>
    </nav>
  </section>

  <footer class="footer-band"></footer>
</div>
</body>
</html>
```